Real Estate Flyer

I would like an A4 size flyer which has the same info 3 times and can be cut into three.
It will be used for letterbox drops for new listings (SELLING) and sold listings (SOLD). The flyer needs a heading (as above) and a space for a photo which is able to be changed for each new property. Needs to be blue, red and white. It also requires my photo, KLT logo, Marisse Thornbury logo and the following text:
"Are you considering selling? Call Marisse today for a complimentary market appraisal".
(KLT logo, Marisse Thornbury Sales Consultant logo and my photo can be found in uploaded files)
Industry/Entity Type
Real Estate
Look and feel

```html
<!DOCTYPE html>
<html lang="en">
<head>
<meta charset="utf-8">
<title>KLT Realty – Letterbox Flyer</title>
<link href="https://fonts.googleapis.com/css2?family=Anton&family=Didact+Gothic&family=Arimo:wght@400;700&display=swap" rel="stylesheet">
<style>
  :root{
    --canvas:#ffffff;
    --ink:#111111;
    --brand-blue:#1f3a78;
    --brand-red:#e3262b;
    --tagline-blue:#2a3fa6;
    --name-grey:#3a3a3a;
    --role-grey:#7a7a7a;
    --body-top:#b3a995;
    --body-bottom:#dcd9d4;
    --header-top:#ffffff;
    --header-bottom:#d9d6d0;
    --frame:#f4f2ee;
  }
  *{box-sizing:border-box;margin:0;padding:0}
  html,body{width:1200px;height:848px;overflow:hidden;background:var(--canvas)}
  .sheet{position:relative;width:1200px;height:848px;overflow:hidden}

  .flyer{
    position:absolute;width:358px;height:738px;overflow:hidden;
    background:linear-gradient(to bottom,var(--body-top) 0%,#c4bcae 45%,var(--body-bottom) 100%);
    box-shadow:0 0 4px rgba(0,0,0,.15);
    font-family:"Arimo",Arial,sans-serif;
  }
  .flyer--one{left:16px;top:43px}
  .flyer--two{left:382px;top:4px;transform:scale(1.13);transform-origin:0 0}
  .flyer--three{left:820px;top:43px}

  .flyer__header{
    position:absolute;left:0;top:0;width:100%;height:107px;
    background:linear-gradient(to bottom,var(--header-top),var(--header-bottom));
  }
  .flyer__status{
    position:absolute;left:100px;top:10px;width:200px;text-align:center;
    font-family:"Anton",Impact,sans-serif;font-weight:400;font-size:31px;letter-spacing:2px;color:var(--ink);line-height:1;
  }
  .brand{
    position:absolute;left:92px;top:60px;height:40px;
    display:flex;align-items:center;gap:10px;
  }
  .brand__mark{width:28px;height:28px;background:var(--brand-red)}
  .brand__name{font-family:"Arimo",Arial,sans-serif;font-weight:700;font-size:27px;color:var(--brand-blue);white-space:nowrap}

  .agent{
    position:absolute;left:13px;top:123px;width:328px;height:108px;
    border:1.5px solid var(--brand-red);
  }
  .agent__photo{position:absolute;left:2px;top:2px;width:70px;height:102px;
    background:linear-gradient(to bottom,#8a8078,#2c2a2e)}
  .agent__name{position:absolute;left:80px;top:14px;font-family:"Didact Gothic",sans-serif;font-size:23px;letter-spacing:1.2px;color:var(--name-grey);white-space:nowrap}
  .agent__role{position:absolute;left:130px;top:42px;font-family:"Didact Gothic",sans-serif;font-size:16px;letter-spacing:1.5px;color:var(--role-grey);white-space:nowrap}
  .agent__phone{position:absolute;left:152px;top:62px;font-size:13px;color:var(--brand-red);white-space:nowrap}

  .tagline{
    position:absolute;left:13px;top:235px;width:336px;
    font-size:16.5px;line-height:1.3;letter-spacing:-.6px;color:var(--tagline-blue);
  }

  .frame{
    position:absolute;border:4px solid var(--frame);border-radius:4px;
    box-shadow:0 0 6px rgba(255,255,255,.9),0 0 2px rgba(0,0,0,.15);
  }
  .frame--hero{left:13px;top:314px;width:185px;height:128px}
  .frame--thumb-a{left:210px;top:314px;width:131px;height:86px}
  .frame--thumb-b{left:210px;top:411px;width:131px;height:86px}
  .frame--thumb-c{left:210px;top:508px;width:131px;height:86px}
  .flyer--three .frame--hero{top:311px;height:171px}
  .flyer--three .frame--thumb-a{top:311px;height:88px}
  .flyer--three .frame--thumb-b{top:408px;height:88px}
  .flyer--three .frame--thumb-c{top:503px;height:88px}
  .frame--empty{background:rgba(255,255,255,.12);border-color:rgba(244,242,238,.7)}

  .photo{width:100%;height:100%}
  .photo--house{background:linear-gradient(to bottom,#ffffff 0%,#8a8782 45%,#b49a78 80%,#5f7a3c 100%)}
  .photo--bedroom{background:linear-gradient(135deg,#f2f2f2,#9c9a98 60%,#3b3836)}
  .photo--dining{background:linear-gradient(135deg,#e9e9e9,#b6b3ae 55%,#6f6b66)}
  .photo--living{background:linear-gradient(135deg,#f0eeea,#a29d95 55%,#2f2c2a)}

  .details{
    position:absolute;left:13px;top:462px;width:185px;height:250px;
    border:4px solid var(--frame);border-radius:6px;
    background:rgba(255,255,255,.08);
    box-shadow:0 0 6px rgba(255,255,255,.9);
    padding:14px 0 0 12px;color:#1c1c1c;
  }
  .details__price{font-size:14.5px;margin-bottom:20px}
  .details__list{list-style:none;font-size:11.5px;line-height:31px;white-space:nowrap}
</style>
</head>
<body>
<main class="sheet">

  <section class="flyer flyer--one">
    <header class="flyer__header">
      <h1 class="flyer__status">SELLING</h1>
      <div class="brand"><span class="brand__mark"></span><span class="brand__name">KLT Realty</span></div>
    </header>
    <div class="agent">
      <div class="agent__photo" role="img" aria-label="Portrait of Marisse Thornbury"></div>
      <p class="agent__name">Marisse Thornbury</p>
      <p class="agent__role">Sales Consultant</p>
      <p class="agent__phone">0400 318 552</p>
    </div>
    <p class="tagline">Are you considering selling? Call Marisse today for a complimentary market appraisal.</p>
    <div class="frame frame--hero"><div class="photo photo--house" role="img" aria-label="Front of the listed two-storey house"></div></div>
    <div class="frame frame--thumb-a"><div class="photo photo--bedroom" role="img" aria-label="Bedroom interior"></div></div>
    <div class="frame frame--thumb-b"><div class="photo photo--dining" role="img" aria-label="Kitchen and dining interior"></div></div>
    <div class="frame frame--thumb-c"><div class="photo photo--living" role="img" aria-label="Living room interior"></div></div>
    <div class="details">
      <p class="details__price">$7,000-$8,000 &nbsp; :)</p>
      <ul class="details__list">
        <li>Amazing big 1980 built</li>
        <li>4 bedroom plus office,</li>
        <li>3 bathroom 4wc,</li>
        <li>reverse cycle air conditioned,</li>
        <li>ingle story home with pool,</li>
        <li>3 car gge and big...</li>
      </ul>
    </div>
  </section>

  <section class="flyer flyer--two">
    <header class="flyer__header">
      <h1 class="flyer__status">SELLING</h1>
      <div class="brand"><span class="brand__mark"></span><span class="brand__name">KLT Realty</span></div>
    </header>
    <div class="agent">
      <div class="agent__photo" role="img" aria-label="Portrait of Marisse Thornbury"></div>
      <p class="agent__name">Marisse Thornbury</p>
      <p class="agent__role">Sales Consultant</p>
      <p class="agent__phone">0400 318 552</p>
    </div>
    <p class="tagline">Are you considering selling? Call Marisse today for a complimentary market appraisal.</p>
    <div class="frame frame--hero"><div class="photo photo--house" role="img" aria-label="Front of the listed two-storey house"></div></div>
    <div class="frame frame--thumb-a"><div class="photo photo--bedroom" role="img" aria-label="Bedroom interior"></div></div>
    <div class="frame frame--thumb-b"><div class="photo photo--dining" role="img" aria-label="Kitchen and dining interior"></div></div>
    <div class="frame frame--thumb-c"><div class="photo photo--living" role="img" aria-label="Living room interior"></div></div>
    <div class="details">
      <p class="details__price">$7,000-$8,000 &nbsp; :)</p>
      <ul class="details__list">
        <li>Amazing big 1980 built</li>
        <li>4 bedroom plus office,</li>
        <li>3 bathroom 4wc,</li>
        <li>reverse cycle air conditioned,</li>
        <li>ingle story home with pool,</li>
        <li>3 car gge and big...</li>
      </ul>
    </div>
  </section>

  <section class="flyer flyer--three">
    <header class="flyer__header">
      <h1 class="flyer__status">SOLD</h1>
      <div class="brand"><span class="brand__mark"></span><span class="brand__name">KLT Realty</span></div>
    </header>
    <div class="agent">
      <div class="agent__photo" role="img" aria-label="Portrait of Marisse Thornbury"></div>
      <p class="agent__name">Marisse Thornbury</p>
      <p class="agent__role">Sales Consultant</p>
      <p class="agent__phone">0400 318 552</p>
    </div>
    <p class="tagline">Are you considering selling? Call Marisse today for a complimentary market appraisal.</p>
    <div class="frame frame--hero frame--empty"></div>
    <div class="frame frame--thumb-a frame--empty"></div>
    <div class="frame frame--thumb-b frame--empty"></div>
    <div class="frame frame--thumb-c frame--empty"></div>
  </section>

</main>
</body>
</html>
```